40k Ultra High Pressure Waterblasing Ad

We need 1 page flyer ad for our industry's brochure/membership directory.
We're a manufacturer & supplier for the Ultra High Pressure Waterblasting industry.
We'd like the ad to be simple and clean, highlighting some of our parts. Our dedication to our customers and affordable prices.
Some of the parts are Dorvel Mastrick Hoses, Sapphire Nozzles, Rotating Jetlance.

Our website is torvaflux.com

Requirements
Must have
• Dorvel Mastrick 40k Hose
• Sapphire Nozzles
• Rotating Jetlance
• **Update - Would like to incorporate the "iron skein logo w/ bulldog" from uploaded dorvel iron skein hose attachment. Highlighting the hose's features.
Nice to have
• Brief Bullet points or something else highlighting what we sell.
• - Pump replacement parts
• - Sapphire Nozzles
• - Rotating Jetlance
• - Fittings and adapters
• - Safety Gear
• I've uploaded past ads we've used.
Should not have
• Lots of text area

```html
<!DOCTYPE html>
<html lang="en">
<head>
<meta charset="utf-8">
<title>Torvaflux Jetting Systems – UHP Flyer</title>
<link rel="stylesheet" href="https://fonts.googleapis.com/css2?family=Oswald:wght@500;700&family=Roboto:wght@400;500;700&display=swap">
<style>
  :root {
    --blue: #1f7fc8;
    --blue-deep: #0f5f9f;
    --blue-light: #6fb8ea;
    --ink: #1d2a36;
    --dark-bg: #24313a;
    --dark-bg-2: #3b4a52;
    --teal-tint: #4d6b72;
    --white: #ffffff;
    --grey-text: #4a5560;
    --silver: #b9c1c7;
  }
  * { box-sizing: border-box; margin: 0; padding: 0; }
  html, body { width: 684px; height: 1200px; overflow: hidden; background: #ffffff; }
  body { font-family: "Roboto", Arial, sans-serif; color: var(--ink); }

  .flyer { position: relative; width: 684px; height: 1200px; overflow: hidden; background: var(--white); }

  .hero-photo {
    position: absolute; left: 0; top: 0; width: 684px; height: 620px;
    background: linear-gradient(135deg, var(--dark-bg) 0%, var(--teal-tint) 45%, var(--dark-bg-2) 75%, #1c252c 100%);
  }

  .wave { position: absolute; left: 0; top: 300px; width: 684px; height: 340px; }

  .brand { position: absolute; left: 40px; top: 40px; display: flex; align-items: center; gap: 14px; }
  .brand-mark { width: 22px; height: 22px; background: var(--blue-light); }
  .brand-name { font-family: "Oswald", Arial, sans-serif; font-weight: 700; font-size: 30px; color: var(--white); letter-spacing: 1px; }
  .brand-sub { position: absolute; left: 40px; top: 92px; font-size: 16px; color: var(--white); font-weight: 500; }

  .headline {
    position: absolute; left: 40px; top: 170px; width: 340px;
    font-family: "Oswald", Arial, sans-serif; font-weight: 700; font-size: 34px; line-height: 1.12;
    color: var(--white); text-transform: uppercase;
  }

  .product-img { position: absolute; border-radius: 6px; }
  .product-label {
    position: absolute; font-size: 15px; font-weight: 700; color: var(--blue-deep);
    display: flex; align-items: center; gap: 6px; white-space: nowrap;
  }
  .tick { width: 16px; height: 16px; flex: none; }

  .img-lance { left: 380px; top: 360px; width: 250px; height: 110px; background: linear-gradient(90deg, #9aa3a9, #dfe4e7 50%, #7d878e); }
  .img-hose { left: 40px; top: 440px; width: 210px; height: 150px; border-radius: 50%; background: radial-gradient(circle, #6d757b 20%, #9aa2a8 45%, #4f575d 80%); }
  .img-nozzles { left: 290px; top: 520px; width: 200px; height: 90px; background: linear-gradient(90deg, #b88a3a, #e2c27a 50%, #a87a2c); }

  .our-products {
    position: absolute; left: 0; top: 690px; width: 300px; height: 44px;
    background: var(--blue); color: var(--white);
    font-size: 19px; font-weight: 700; padding: 11px 0 0 40px;
    clip-path: polygon(0 0, 92% 0, 100% 100%, 0 100%);
  }
  .products-rule { position: absolute; left: 0; top: 734px; width: 684px; height: 3px; background: var(--blue); }

  .img-pump { left: 40px; top: 790px; width: 180px; height: 130px; background: radial-gradient(circle, #cfd5d9 15%, #8c969d 60%, #6b747a); }
  .img-fittings { left: 260px; top: 790px; width: 170px; height: 130px; background: linear-gradient(135deg, #a87a2c, #e4c57f 50%, #8f9aa1); }
  .img-gear { left: 470px; top: 770px; width: 180px; height: 170px; background: linear-gradient(180deg, #2e3a44, #48586a 55%, #1e252b); }

  .footer-rule { position: absolute; left: 40px; top: 1040px; width: 604px; height: 2px; background: var(--silver); }
  .contact-call { position: absolute; left: 40px; top: 1070px; display: flex; align-items: center; gap: 12px; }
  .contact-call .phone-icon { width: 40px; height: 40px; }
  .call-prompt { font-size: 14px; color: var(--grey-text); font-weight: 500; }
  .call-number { font-family: "Oswald", Arial, sans-serif; font-size: 30px; font-weight: 700; color: var(--ink); line-height: 1.1; }

  .contact-lines { position: absolute; left: 330px; top: 1074px; font-size: 14px; color: var(--grey-text); line-height: 1.9; }
  .contact-lines span { display: flex; align-items: center; gap: 8px; }
  .dot { width: 12px; height: 12px; border-radius: 50%; background: var(--blue); }

  .follow { position: absolute; left: 520px; top: 1088px; display: flex; align-items: center; gap: 10px; font-size: 14px; font-weight: 700; color: var(--ink); }
  .social-box { width: 26px; height: 26px; background: var(--blue-deep); border-radius: 3px; }
</style>
</head>
<body>
<main class="flyer">
  <div class="hero-photo" role="img" aria-label="Dark industrial photo of UHP waterblasting pump machinery"></div>

  <svg class="wave" viewBox="0 0 684 340" preserveAspectRatio="none" aria-hidden="true">
    <path d="M0 250 C 200 300, 420 120, 684 40 L684 340 L0 340 Z" fill="#ffffff"/>
    <path d="M0 236 C 200 286, 420 106, 684 26" fill="none" stroke="#1f7fc8" stroke-width="10"/>
    <path d="M0 218 C 210 268, 430 90, 684 8" fill="none" stroke="#6fb8ea" stroke-width="4"/>
  </svg>

  <div class="brand">
    <span class="brand-mark"></span>
    <span class="brand-name">TORVAFLUX</span>
  </div>
  <div class="brand-sub">Torvaflux Jetting Systems, Inc.</div>

  <h1 class="headline">Supplying the essentials in the UHP surface preparation industry</h1>

  <div class="product-img img-lance" role="img" aria-label="Rotating jetlance tool"></div>
  <div class="product-label" style="left:470px; top:482px;">
    <svg class="tick" viewBox="0 0 16 16"><path d="M2 8 L6 12 L14 3" fill="none" stroke="#1f7fc8" stroke-width="2.5"/></svg>Rotating Jetlance
  </div>

  <div class="product-img img-hose" role="img" aria-label="Coiled Dorvel Mastrick 40k hose"></div>
  <div class="product-label" style="left:40px; top:604px;">
    <svg class="tick" viewBox="0 0 16 16"><path d="M2 8 L6 12 L14 3" fill="none" stroke="#1f7fc8" stroke-width="2.5"/></svg>Dorvel Mastrick 40k Hose
  </div>

  <div class="product-img img-nozzles" role="img" aria-label="Brass sapphire nozzles"></div>
  <div class="product-label" style="left:310px; top:622px;">
    <svg class="tick" viewBox="0 0 16 16"><path d="M2 8 L6 12 L14 3" fill="none" stroke="#1f7fc8" stroke-width="2.5"/></svg>Sapphire Nozzles
  </div>

  <div class="our-products">Our Products</div>
  <div class="products-rule"></div>

  <div class="product-img img-pump" role="img" aria-label="Pump replacement parts"></div>
  <div class="product-label" style="left:40px; top:940px;">
    <svg class="tick" viewBox="0 0 16 16"><path d="M2 8 L6 12 L14 3" fill="none" stroke="#1f7fc8" stroke-width="2.5"/></svg>Pump replacement parts
  </div>

  <div class="product-img img-fittings" role="img" aria-label="Fittings and adapters"></div>
  <div class="product-label" style="left:260px; top:940px;">
    <svg class="tick" viewBox="0 0 16 16"><path d="M2 8 L6 12 L14 3" fill="none" stroke="#1f7fc8" stroke-width="2.5"/></svg>Fittings and adapters
  </div>

  <div class="product-img img-gear" role="img" aria-label="Protective safety suit, boots and gloves"></div>
  <div class="product-label" style="left:500px; top:960px;">
    <svg class="tick" viewBox="0 0 16 16"><path d="M2 8 L6 12 L14 3" fill="none" stroke="#1f7fc8" stroke-width="2.5"/></svg>Safety Gear
  </div>

  <div class="footer-rule"></div>

  <div class="contact-call">
    <svg class="phone-icon" viewBox="0 0 40 40" aria-hidden="true">
      <path d="M10 5 L16 5 L18 13 L14 16 C16 21 19 24 24 26 L27 22 L35 24 L35 30 C35 33 33 35 30 35 C17 34 6 23 5 10 C5 7 7 5 10 5 Z" fill="#1d2a36"/>
    </svg>
    <div>
      <div class="call-prompt">Have a question? Call Us</div>
      <div class="call-number">555-014-2290</div>
    </div>
  </div>

  <div class="contact-lines">
    <span><i class="dot"></i>info@torvaflux.com</span>
    <span><i class="dot"></i>www.torvaflux.com</span>
  </div>

  <div class="follow">
    FOLLOW US
    <span class="social-box"></span>
    <span class="social-box"></span>
  </div>
</main>
</body>
</html>
```